Re-design of website: www.velmarpromo.ca/en/

Velmar Promo is a promotional agency specializing in on-site marketing. We are re-designing their website.

We have already produced a prototype:
http://borquelab.com/velmarpromo_siteweb/

The architecture in the prototype must be respected. Please dress up the design with green, grey and black circles and other textures found on their current website www.velmarpromo.ca

Inspiration for design that we like, clean, flat design:

- http://www.tundrafolk.co/
- http://quillborough.com/#!/process
- http://wearedelvani.com/

Delivrables: PSD files of each page of the prototype

Here are the images of their print portfolio: http://ftp.velmarpromo.ca/clients/VMP/VELMARPROMO-PORTFOLIO-2012_EN.zip

Industry/Entity Type

Architecture

Requirements
Must have
• Responsive Design

```html
<!DOCTYPE html>
<html lang="fr">
<head>
<meta charset="utf-8">
<title>Velmar Promo</title>
<link rel="stylesheet" href="https://fonts.googleapis.com/css2?family=Alfa+Slab+One&family=Bree+Serif&family=PT+Serif:wght@400;700&family=Arimo:wght@400;700&display=swap">
<style>
:root{
  --green:#9fd06a;
  --green-soft:#a6c97e;
  --green-dark:#6fae3a;
  --grey-title:#7d7d7d;
  --grey-dark:#3a3a3a;
  --grey-ring:#8a8a8a;
  --grey-foot:#e0e0e0;
  --grey-bar:#5b5b5b;
  --text:#1f1f1f;
  --muted:#6b6b6b;
  --white:#ffffff;
}
*{margin:0;padding:0;box-sizing:border-box}
html,body{width:800px;height:1200px;overflow:hidden;background:var(--white)}
body{position:relative;font-family:"Arimo",Arial,sans-serif;color:var(--text)}
.abs{position:absolute}

.lang{left:670px;top:6px;font-size:10px;color:#444}
.brand{left:0;width:800px;top:22px;display:flex;justify-content:center;align-items:center;gap:12px}
.brand-name{font-family:"Alfa Slab One",serif;font-size:30px;color:var(--grey-dark);letter-spacing:1px}
.brand-dot{width:26px;height:26px;border-radius:50%;background:var(--green)}

.nav{left:0;top:80px;width:800px;height:34px;background:var(--green)}
.nav-item{position:absolute;top:12px;font-size:9.5px;color:#fff;text-transform:uppercase;white-space:nowrap}
.nav-item.current{opacity:.85}
.n1{left:102px}.n2{left:155px}.n3{left:216px}.n4{left:302px}.n5{left:380px}.n6{left:461px}
.social{position:absolute;left:587px;top:5px;display:flex;gap:5px}
.social span{width:24px;height:24px;display:block}
.social .s1{background:#3b5a99}.social .s2{background:#2ba8e0}.social .s3{background:#cc2020}.social .s4{background:#1777b5}

.hero{left:0;top:114px;width:800px;height:234px;background:linear-gradient(90deg,#eceeed 0%,#f6f6f4 35%,#e5e6e2 70%,#d9dad6 100%)}
.hero-text{left:88px;top:54px;width:340px;font-family:"PT Serif",Georgia,serif;font-size:15.5px;line-height:19px;color:var(--text);white-space:nowrap}
.hero-text strong{font-size:18.5px;font-weight:700;letter-spacing:.3px}
.learn{left:307px;top:178px;font-family:"PT Serif",Georgia,serif;font-weight:700;font-size:15px;color:var(--green-dark);letter-spacing:.5px}
.hero-photos{left:432px;top:28px;width:312px;height:160px;background:linear-gradient(135deg,#f3f3f3,#d8d2c8 50%,#c85050 100%);opacity:.9}

.section-title{left:100px;top:380px;font-family:"Alfa Slab One",serif;font-size:30px;color:var(--grey-title);letter-spacing:.5px;white-space:nowrap}
.section-num{left:100px;top:414px;font-family:"Alfa Slab One",serif;font-size:50px;color:var(--green)}

.tile{width:288px;height:158px}
.t1{left:101px;top:501px;background:linear-gradient(135deg,#bcdc98,#a6cf7a);border:1px solid #b8d497}
.t2{left:410px;top:501px;background:linear-gradient(135deg,#dfe4ea,#b9c3cc 60%,#e6e6e6)}
.t3{left:101px;top:690px;background:linear-gradient(135deg,#2a4e78,#d8dde3 50%,#1a1a1a)}
.t4{left:410px;top:690px;background:linear-gradient(135deg,#6a4a33,#b8a58c 50%,#3a2a20)}
.tile-icons{position:absolute;left:94px;top:54px;display:flex;gap:10px}
.tile-icons svg{display:block}

.footer{left:0;top:888px;width:800px;height:282px;background:var(--grey-foot)}
.col-title{font-family:"Bree Serif",serif;font-size:21px;color:#555;font-weight:400;white-space:nowrap}
.ct1{left:100px;top:12px}.ct2{left:360px;top:8px}.ct3{left:565px;top:12px}
.ring{width:152px;height:152px;border-radius:50%;background:var(--green-soft);color:#fff;display:flex;flex-direction:column;justify-content:center}
.r1{left:101px;top:48px;border:10px solid var(--grey-dark);padding-left:16px;font-size:8.5px;line-height:14px;white-space:nowrap}
.r2{left:334px;top:48px;border:10px solid var(--grey-ring);align-items:center;text-align:center}
.r3{left:545px;top:48px;border:10px solid var(--grey-ring);padding:0 14px 0 22px}
.r2 .small{font-size:13px}
.r2 .big{font-size:32px;line-height:34px;letter-spacing:.5px}
.r2 .role{font-size:10px;margin-top:6px}
.r2 .cta{font-size:11px;font-weight:700;color:#111;text-decoration:underline;margin-top:8px}
.r3 .handle{font-size:14px;color:#111;margin-bottom:4px}
.r3 .blurb{font-size:9px;line-height:12px}
.col-text{width:170px;top:210px;font-size:8.5px;line-height:12px;color:var(--muted)}
.x1{left:101px}.x2{left:334px}.x3{left:545px}

.bottom{left:0;top:1170px;width:800px;height:30px;background:var(--grey-bar)}
.bottom p{position:absolute;left:102px;top:9px;font-size:9.5px;color:#fff}
</style>
</head>
<body>
<div class="abs lang">English</div>
<header class="abs brand"><span class="brand-name">Velmar Promo</span><span class="brand-dot"></span></header>

<nav class="abs nav">
  <span class="nav-item current n1">Agence</span>
  <span class="nav-item n2">Services</span>
  <span class="nav-item n3">Realisations</span>
  <span class="nav-item n4">Evenements</span>
  <span class="nav-item n5">Recrutement</span>
  <span class="nav-item n6">Contact</span>
  <div class="social" aria-label="Réseaux sociaux"><span class="s1"></span><span class="s2"></span><span class="s3"></span><span class="s4"></span></div>
</nav>

<section class="abs hero">
  <p class="abs hero-text"><strong>EXTRAORDINARY, MEMORABLE,</strong><br>and fully integrated promotions. Commit-<br>ted to exciting consumers and surprising<br>our clients. All at once. Dedicated to achiev-<br>ing results. All the time. Since 1999.</p>
  <a class="abs learn">LEARN MORE</a>
  <div class="abs hero-photos" role="img" aria-label="Collage of in-store promotion sketches and photos of staffed product displays"></div>
</section>

<h2 class="abs section-title">NOS RÉALISATIONS</h2>
<div class="abs section-num">360</div>

<div class="abs tile t1" role="img" aria-label="Green-tinted sketch of a branded retail booth">
  <div class="tile-icons">
    <svg width="48" height="48" viewBox="0 0 48 48"><rect x="1.5" y="1.5" width="45" height="45" fill="none" stroke="#fff" stroke-width="3"/><circle cx="22" cy="21" r="7" fill="none" stroke="#fff" stroke-width="2.5"/><line x1="27" y1="26" x2="34" y2="33" stroke="#fff" stroke-width="3"/></svg>
    <svg width="48" height="48" viewBox="0 0 48 48"><rect x="1.5" y="1.5" width="45" height="45" fill="none" stroke="#fff" stroke-width="3"/><polygon points="18,14 34,24 18,34" fill="#fff"/></svg>
  </div>
</div>
<div class="abs tile t2" role="img" aria-label="Collage of store display renderings and event equipment"></div>
<div class="abs tile t3" role="img" aria-label="Collage of contest posters and web promotion screens"></div>
<div class="abs tile t4" role="img" aria-label="Collage of promotional staff serving tastings in venues"></div>

<footer class="abs footer">
  <h3 class="abs col-title ct1">Nous Contacter</h3>
  <h3 class="abs col-title ct2">Appliquer</h3>
  <h3 class="abs col-title ct3">Suivez-nous</h3>

  <div class="abs ring r1"><p>2290, Alder street,<br>unit 204 Montreal,<br>Quebec&nbsp; H2X 3K7<br>Velmar Promo 514-555-0142<br>Velmar Promo 514-555-0187</p></div>
  <div class="abs ring r2"><span class="small">We are</span><span class="big">HIRING</span><span class="role">Designser</span><span class="cta">Click Here</span></div>
  <div class="abs ring r3"><span class="handle">/velmarpromo</span><span class="blurb">Lorem Ipsum. Proin gravida nibh vel velit auctor aliquet. Aenean sollicitudin, lorem quis bibendum auctor, nisi</span></div>

  <p class="abs col-text x1">Lorem Ipsum. Proin gravida nibh vel velit auctor aliquet. Aenean sollicitudin, lorem quis bibendum auctor, nisi elit consequat ipsum, nec sagittis sem nibh id elit. Duis sed odio sit amet nibh vulputate cursus a sit amet mauris. Morbi accumsan ipsum</p>
  <p class="abs col-text x2">Lorem Ipsum. Proin gravida nibh vel velit auctor aliquet. Aenean sollicitudin, lorem quis bibendum auctor, nisi elit consequat ipsum, nec sagittis sem nibh id elit. Duis sed odio sit amet nibh vulputate</p>
  <p class="abs col-text x3">Lorem Ipsum. Proin gravida nibh vel velit auctor aliquet. Aenean sollicitudin, lorem quis bibendum auctor, nisi elit consequat ipsum, nec sagittis sem nibh id elit. Duis sed odio sit amet nibh vulputate cursus a sit</p>
</footer>

<div class="abs bottom"><p>(c) Velmar Promo. Tous droits réservés.</p></div>
</body>
</html>
```